landing pages for BidPanel split testing

professional services

tattoo studio

SPA

We need to improve conversions, load speed and lumo ads quality score to be priority

Content is ready copy and visual

Just need a few extra ideas to test

https://ridgewaypartners.com.au/

Current website

https://property.ridgewaypartners.com.au/

1 landing page for ads

We would like to test something a little visually pleasing while in the past simple even ugly has work we are missing the mark

https://byvelo.co/?utm_source=LumoSearchNetwork&utm_medium=cpc&utm_device=m&utm_campaign=30000028802&utm_adgroup=274801592443&utm_keyword=buyers%20agent&utm_matchtype=p&utm_placement=&utm_adposition=&utm_location=8284267&keyword_k=buyers%20agent&utm_term=buyers%20agent&gclid={var:gclid}&gad_source=1&gclid=DkxLDBkxrsf2CiBrFjxB8h0Rij-gPpTytbZaphPxBtgIB2dQV81tsyOyscSyR_Er_LyCirWuvUgyuSpDnvxRBwE_CxCF

Here are the biggest ad spends in the market to date

Target Market(s)

People who are looking to get into the property market either invest or.home who want the head ache of negotiation gone, or don't know where to look , building wealth through property

Industry/Entity Type

Investment property buyers Agent

Coding

Coded - Design and coding required

Font styles to use
Other font styles liked:
• Keep to current

Requirements
Must have
• Don't change our copy for the ads landing page just need to flow better placement etc with call to action, remove the long winded steps , as some.more examples of example.properties
Nice to have
• Call to actions placed as they are ( keep to the original websites colour scheme )
Should not have
• Remove and reference to financial planning

```html
<!DOCTYPE html>
<html lang="en">
<head>
<meta charset="utf-8">
<title>Ridgeway Partners – Investment Property</title>
<link href="https://fonts.googleapis.com/css2?family=Cabin:wght@400;500;600;700&family=Roboto:wght@300;400;500;700&display=swap" rel="stylesheet">
<style>
:root{
  --navy:#0b3a5c;
  --navy-dark:#06304f;
  --ink:#222;
  --muted:#444;
  --white:#fff;
  --footer:#121212;
  --star:#f5b91a;
}
*{box-sizing:border-box;margin:0;padding:0}
html,body{width:1200px;height:3583px;overflow:hidden;background:var(--white)}
body{position:relative;font-family:'Roboto',sans-serif;color:var(--ink)}
.abs{position:absolute}
.heading{font-family:'Cabin',sans-serif;font-weight:400;color:var(--ink)}
.heading strong,.accent{color:var(--navy);font-weight:500}
.btn{position:absolute;display:flex;align-items:center;justify-content:center;border-radius:24px;font-family:'Roboto',sans-serif;font-weight:500;font-size:15px;text-transform:uppercase;text-decoration:none}
.btn-solid{background:var(--navy);color:var(--white)}
.btn-outline{border:2px solid var(--navy);color:var(--navy);background:var(--white)}
.btn-light{background:var(--white);color:var(--navy-dark)}

/* hero */
.hero{position:absolute;left:0;top:0;width:1200px;height:585px;overflow:hidden;
  background:linear-gradient(90deg,rgba(255,255,255,.92) 0%,rgba(255,255,255,.75) 38%,rgba(255,255,255,0) 55%),
  linear-gradient(180deg,#c9d7e3 0%,#8ea3b5 45%,#6f8a55 75%,#4d6a33 100%)}
.brand{font-family:'Cabin',sans-serif;font-weight:600;color:var(--navy);letter-spacing:6px;display:flex;align-items:center;gap:10px}
.brand-dot{width:34px;height:34px;border-radius:50%;background:var(--navy)}
.hero .brand{left:111px;top:34px;font-size:38px}
.hero-lead{left:111px;top:163px;width:425px;font-size:15.5px;line-height:25px;color:var(--ink)}
.hero-title{left:110px;top:226px;width:420px;font-size:37px;line-height:43px}
.hero-title strong{font-weight:700}

/* intro */
.photo{position:absolute}
.intro-title{left:623px;top:652px;width:520px;font-size:41px;line-height:47px}
.points{left:628px;top:826px;width:440px;font-size:15px;line-height:25px;color:var(--muted)}
.point{position:relative;padding-left:36px;margin-bottom:14px}
.point svg{position:absolute;left:0;top:50%;margin-top:-12px}

/* stories */
.section-title{position:absolute;left:0;width:1200px;text-align:center;font-size:42px}
.stories{left:0;top:1329px;width:1200px;height:639px;background:var(--navy-dark)}
.story-title{left:111px;top:64px;width:460px;font-size:36px;line-height:46px;color:var(--white)}
.stars{left:111px;top:188px;display:flex;gap:5px}
.story-text{left:112px;top:232px;width:420px;font-size:15.5px;line-height:26px;color:var(--white)}
.story-text p{margin-bottom:14px}
.author{left:111px;top:497px;display:flex;align-items:center;gap:14px;color:var(--white);font-size:15px}
.author b{font-size:19px}
.avatar{width:75px;height:75px;border-radius:50%;background:linear-gradient(135deg,#e6a27a,#b56a44)}
.arrow{position:absolute;width:40px;height:40px;border-radius:50%;display:flex;align-items:center;justify-content:center}

/* wins */
.win-card{left:142px;top:2262px;width:449px;height:450px;background:var(--white);border-radius:22px}
.stat{position:absolute;width:200px}
.stat-label{font-family:'Cabin',sans-serif;font-size:20px;line-height:24px;color:var(--ink)}
.stat-value{font-family:'Roboto',sans-serif;font-weight:300;font-size:34px;color:var(--navy);line-height:44px;white-space:nowrap}
.stat-note{font-size:14.5px;color:var(--ink);line-height:21px}
.win-copy{left:38px;top:232px;width:380px;font-size:12px;line-height:19.5px;color:var(--ink)}
.win-copy p{margin-bottom:9px}

/* cta */
.cta{left:0;top:2910px;width:1200px;height:288px;background:var(--navy-dark);color:var(--white);text-align:center}
.cta h2{position:absolute;left:0;top:68px;width:1200px;font-family:'Cabin',sans-serif;font-weight:500;font-size:44px}
.cta p{position:absolute;left:0;top:134px;width:1200px;font-size:16px}

/* footer */
.footer{left:0;top:3198px;width:1200px;height:385px;background:var(--footer);color:var(--white)}
.footer .brand{left:0;width:1200px;justify-content:center;top:84px;font-size:62px;color:var(--white);letter-spacing:10px}
.footer .brand-dot{width:54px;height:54px;background:var(--white)}
.contact{position:absolute;top:223px;display:flex;gap:18px;font-size:15px;line-height:23px}
.contact b{font-size:20px;font-weight:700;display:block;line-height:24px}
.contact .ico{width:44px;height:44px;border-radius:50%;background:var(--white);display:flex;align-items:center;justify-content:center;flex-shrink:0;margin-top:6px}
.copyright{position:absolute;left:0;top:3527px;width:1200px;text-align:center;font-size:15px;color:var(--white)}
</style>
</head>
<body>

<section class="hero">
  <div class="abs brand"><span class="brand-dot"></span>RIDGEWAY</div>
  <p class="abs hero-lead">Under-the-Radar Properties that Bring More Profit, Supported by Research, Insights, and Market Analysis</p>
  <h1 class="abs heading hero-title"><strong>DISCOVER</strong> Real Estate Investment Opportunities in Australia With Greater Returns</h1>
  <div role="img" aria-label="Photo of a blue weatherboard family home with white garage and porch, surrounded by trees" class="abs" style="left:520px;top:0;width:680px;height:585px;background:linear-gradient(160deg,#dfe8ef 0%,#6e8aa3 35%,#5b7690 55%,#e7e7e2 75%,#5a7a3c 100%);opacity:.55"></div>
  <a class="btn btn-solid" style="left:111px;top:410px;width:291px;height:42px">Book a free investment call</a>
</section>

<div role="img" aria-label="Photo of a navy two-storey house with a paved front path" class="photo" style="left:111px;top:673px;width:373px;height:432px;background:linear-gradient(180deg,#5f7f9a 0%,#2f3f63 45%,#d9d6cf 75%,#8a8a80 100%)"></div>
<div role="img" aria-label="Photo of a hand holding a small model house at sunset" class="photo" style="left:282px;top:826px;width:271px;height:317px;background:linear-gradient(180deg,#2a3a55 0%,#7b6a6a 45%,#d39a5c 65%,#3f4a2a 100%);border-left:4px solid #fff;border-top:4px solid #fff"></div>

<h2 class="abs heading intro-title"><span class="accent">Overlooked Investment Opportunities</span> That Deliver Greater ROI</h2>
<div class="abs points">
  <div class="point"><svg width="24" height="24" viewBox="0 0 24 24"><circle cx="12" cy="12" r="12" fill="var(--navy)"/><path d="M7 12.5l3.2 3.2L17 9" stroke="#fff" stroke-width="2.4" fill="none"/></svg>Unlike others, we don't push our property book filled with developer stock.</div>
  <div class="point"><svg width="24" height="24" viewBox="0 0 24 24"><circle cx="12" cy="12" r="12" fill="var(--navy)"/><path d="M7 12.5l3.2 3.2L17 9" stroke="#fff" stroke-width="2.4" fill="none"/></svg>Instead, we uncover small, hidden gems – properties with untapped potential for maximum returns, in markets most agents don't even know about.</div>
  <div class="point" style="margin-top:-6px">What does it cost to see if this is the right solution for you? Absolutely nothing</div>
</div>
<a class="btn btn-solid" style="left:623px;top:1066px;width:291px;height:42px">Book a free, no-obligation call</a>
<a class="btn btn-outline" style="left:929px;top:1066px;width:118px;height:42px">Read more</a>

<h2 class="heading section-title" style="top:1218px"><span class="accent">Success</span> Stories</h2>

<section class="abs stories">
  <h3 class="abs story-title" style="font-family:'Cabin',sans-serif;font-weight:400">Smart Investment, Massive Profits</h3>
  <div class="abs stars">
    <svg width="150" height="28" viewBox="0 0 150 28"><g fill="var(--star)"><path id="st" d="M14 1l3.8 8.3 9 .9-6.8 6 2 8.9L14 20.5 6 25.1l2-8.9-6.8-6 9-.9z"/><use href="#st" x="31"/><use href="#st" x="62"/><use href="#st" x="93"/><use href="#st" x="124"/></g></svg>
  </div>
  <div class="abs story-text">
    <p>Prices almost doubled on both my lots. I sold one before it settled without making a single loan repayment and made $150,000.</p>
    <p>I held the second and sold it lasy Year for near enough $300,000 profit,these properties where under $600,000 when we signed the first contract .this was a time when everyone wa walking about investing in sydney and melbourne .i paid half the price for my investment and made likely more than everyone who opted for hype.</p>
  </div>
  <div class="abs author"><span class="avatar" role="img" aria-label="Client portrait"></span><span><b>Marcus</b>, Kogarah</span></div>
  <div class="arrow" style="left:38px;top:339px;border:2px solid #fff"><svg width="14" height="14" viewBox="0 0 14 14"><path d="M9 2L4 7l5 5" stroke="#fff" stroke-width="2" fill="none"/></svg></div>
  <div role="img" aria-label="Photo of a street of suburban houses under a cloudy blue sky" class="abs" style="left:624px;top:0;width:576px;height:639px;background:linear-gradient(180deg,#6f9fcf 0%,#b7cde0 45%,#c9c2b0 70%,#6f8a55 88%,#9a968c 100%)"></div>
  <div class="arrow" style="left:1115px;top:339px;background:#fff"><svg width="14" height="14" viewBox="0 0 14 14"><path d="M5 2l5 5-5 5" stroke="#222" stroke-width="2" fill="none"/></svg></div>
</section>

<h2 class="heading section-title" style="top:2048px"><span class="accent">Our Recent</span> Wins</h2>

<div role="img" aria-label="Photo of a beige house with a double white garage, lawn and pine trees" class="abs" style="left:111px;top:2150px;width:978px;height:670px;background:linear-gradient(180deg,#9fb9d1 0%,#b8b09c 30%,#cfc8b8 55%,#8c8678 78%,#5f9a3a 100%)"></div>
<div class="abs win-card">
  <div class="stat" style="left:35px;top:18px">
    <div class="stat-label">NOOSA HEADS</div>
    <div class="stat-value" style="margin-top:6px">$ 575,000</div>
    <div class="stat-note" style="margin-top:4px">Purchase Price (2018)</div>
  </div>
  <div class="stat" style="left:251px;top:18px">
    <div class="stat-label">NOOSA HEADS</div>
    <div class="stat-value" style="margin-top:6px">13.10%</div>
    <div class="stat-note" style="margin-top:4px;padding-left:9px">Compounded Annual<br>Growth Rate</div>
  </div>
  <div class="stat" style="left:35px;top:148px">
    <div class="stat-value">$ 1,280,000</div>
    <div class="stat-note" style="margin-top:6px;padding-left:4px">Estimated Value (July 2024)</div>
  </div>
  <div class="stat" style="left:251px;top:148px">
    <div class="stat-value">4.4%</div>
    <div class="stat-note" style="margin-top:6px">Rental Yield</div>
  </div>
  <div class="abs win-copy">
    <p>Still against units and townhouses? We secured a client 2 of these units back in 2018. Even before settlement or a single repayment, the client had already sold one for a profit of $150,000. The other unit was sold for $820,000 early 2021.</p>
    <p>Fast forward to today, both of these units are valued well over $1.2 million each while earning aboveaverage rental yields compared to other apartments in the area. With the right strategy, units and townhouses can easily deliver exceptional returns and outperform market expectations.</p>
  </div>
</div>

<section class="abs cta">
  <h2>Ready to discover your next lucrative investment?</h2>
  <p>Contact Ridgeway Partners today and see why savvy investors choose us over traditional agents.</p>
  <a class="btn btn-light" style="left:438px;top:177px;width:289px;height:42px">Book a free investment call</a>
</section>

<footer class="abs footer">
  <div class="abs brand"><span class="brand-dot"></span>RIDGEWAY</div>
  <div class="contact" style="left:206px">
    <span class="ico"><svg width="22" height="16" viewBox="0 0 22 16"><rect width="22" height="16" rx="2" fill="#121212"/><path d="M1 1l10 8 10-8" stroke="#fff" stroke-width="1.6" fill="none"/></svg></span>
    <div><b>Email:</b>info@ridgewaypartners.<br>com.au</div>
  </div>
  <div class="contact" style="left:533px">
    <span class="ico"><svg width="18" height="24" viewBox="0 0 18 24"><path d="M9 0C4 0 0 4 0 9c0 7 9 15 9 15s9-8 9-15c0-5-4-9-9-9z" fill="#121212"/><circle cx="9" cy="9" r="3.4" fill="#fff"/></svg></span>
    <div><b>Location:</b>14/88 Harbour Rd, Brisbane<br>QLD 4000</div>
  </div>
  <div class="contact" style="left:836px">
    <span class="ico"><svg width="20" height="20" viewBox="0 0 24 24"><path d="M6.6 10.8a15 15 0 006.6 6.6l2.2-2.2c.3-.3.7-.4 1-.2 1.1.4 2.300.6 3.6.6.6 0 1 .4 1 1V20c0 .6-.4 1-1 1A17 17 0 013 4c0-.6.4-1 1-1h3.5c.6 0 1 .4 1 1 0 1.3.2 2.5.6 3.6.1.3 0 .7-.2 1z" fill="#121212"/></svg></span>
    <div><b>Phone No:</b>(02) 5550 1482</div>
  </div>
</footer>
<div class="copyright">Copyright © 2024 Ridgeway | All Rights Reserved</div>

</body>
</html>
```